PSD website for property company

Please read the brief thoroughly.

We are looking for a new website for a property group that does property acquisitions, property development and property management.
They buy, build and lease core inner city industrial assets in Sydney, Australia.
They also invest in residential developments.

Site menu
- Home page
- Property – sub menus include – Leasing ; Projects ; Investments ; Property Management
- Capital and finance
- About
- Contact

They like this website
https://www.velmorn.com.au/

They want the site to be clean, modern and bold.
They like few colors, even black and white is OK to submit

They have a logo and style guide and useable images here:
http://www.quorvex.net/temp/PellikWeb2019.zip
The zip file is also attached to this project.
We have supplied some images to give you an idea, but we will also require you to provide at least 3 extra images from stock photos.
Use your imagination.

I am expecting a lot of similar designs, so be aware the photos you choose will be really important.
They want really 3 good stock photos used and supplied without charge.
Please not too generic, I repeat the quality of the photos is important.
You may provide several photos (but not in multiple submissions please) and we will choose the best three to be provided.

The winner will be selected on a single home page design and required to provide;
All photos use in original format without charge
A second ‘standard page’ template design based on the winning home page design

```html
<!DOCTYPE html>
<html lang="en">
<head>
<meta charset="utf-8">
<title>Pellik — Your Property Solution</title>
<link href="https://fonts.googleapis.com/css2?family=Arimo:wght@400;700&display=swap" rel="stylesheet">
<style>
:root{
  --green:#566f2e;
  --green-text:#4f6a24;
  --ink:#222;
  --muted:#777;
  --white:#fff;
  --line:#333;
  --hero-sky:#b9c4cc;
  --hero-brick:#5b4a3e;
  --news-dark:#4a4845;
}
*{box-sizing:border-box;margin:0;padding:0}
html,body{width:1200px;height:3602px;overflow:hidden}
body{font-family:"Arimo",Arial,sans-serif;color:var(--ink);background:var(--white);position:relative}
.abs{position:absolute}
.photo{position:absolute}

/* hero */
.hero{position:absolute;left:0;top:0;width:1200px;height:778px;
  background:linear-gradient(180deg,#c3ccd3 0%,#a7b0b3 35%,#6d5d50 62%,#4a4036 82%,#8a8c8e 100%)}
.logo{position:absolute;font-weight:700;letter-spacing:.28em}
.hero .logo{left:81px;top:32px;font-size:29px;color:var(--white)}
.nav{position:absolute;right:83px;top:37px;display:flex;gap:27px;list-style:none}
.nav a{color:var(--white);text-decoration:none;font-size:15px}
.bracket{position:absolute;left:400px;width:411px;height:93px;border:16px solid var(--white)}
.bracket.top{top:217px;border-bottom:none}
.bracket.bottom{top:474px;border-top:none}
.hero-title{position:absolute;left:0;width:1200px;top:334px;text-align:center;
  color:var(--white);font-weight:700;font-size:51px;letter-spacing:.01em}

/* buttons */
.btn{position:absolute;display:flex;align-items:center;justify-content:center;gap:14px;
  font-size:15px;text-decoration:none;border:2px solid var(--line);color:var(--ink)}
.btn.light{border-color:var(--white);color:var(--white)}
.btn svg{width:18px;height:14px}

/* intro */
.intro-title{position:absolute;left:0;width:1200px;top:840px;text-align:center;
  color:var(--green-text);font-weight:700;font-size:33px;line-height:40px}
.intro-sub{position:absolute;left:0;width:1200px;top:950px;text-align:center;color:var(--muted);font-size:14px}
.card-title{position:absolute;top:1260px;color:var(--green-text);font-weight:700;font-size:28px}
.card-text{position:absolute;top:1312px;width:330px;color:var(--muted);font-size:13.5px;line-height:24px}

/* capital band */
.capital{position:absolute;left:0;top:1557px;width:607px;height:397px;background:var(--green)}
.capital h2{position:absolute;left:81px;top:48px;color:var(--white);font-size:32px;font-weight:700}
.capital p{position:absolute;left:81px;top:111px;width:410px;color:var(--white);font-size:13.5px;line-height:24px}

.section-title{position:absolute;left:0;width:1200px;text-align:center;color:var(--green-text);font-weight:700;font-size:33px}

/* newsletter */
.news{position:absolute;left:0;top:2843px;width:1200px;height:602px;
  background:linear-gradient(180deg,#55524e 0%,var(--news-dark) 55%,#3f3d3a 100%)}
.news h2{position:absolute;left:0;width:1200px;top:76px;text-align:center;color:var(--white);font-size:31px;font-weight:700}
.field{position:absolute;left:329px;width:545px;border:2px solid var(--white);color:var(--white);
  font-size:14px;padding:0 22px;display:flex;align-items:center}
.field.msg{align-items:flex-start;padding-top:18px}

/* footer */
.footer .logo{left:129px;top:3482px;font-size:38px;color:var(--green)}
.footer-links{position:absolute;top:3494px;font-size:14px;color:var(--ink)}
.divider{position:absolute;left:643px;top:3488px;width:2px;height:28px;background:var(--ink)}
.social{position:absolute;top:3496px;width:14px;height:14px;border-radius:50%;background:var(--ink)}
.copyright{position:absolute;left:0;width:1200px;top:3548px;text-align:center;font-size:14px;color:var(--ink)}
</style>
</head>
<body>

<header class="hero">
  <div class="photo" role="img" aria-label="Brick apartment building with arched ground floor shops on a tree-lined street" style="inset:0"></div>
  <div class="logo">PELLIK</div>
  <ul class="nav">
    <li><a href="#">Home</a></li>
    <li><a href="#">Property</a></li>
    <li><a href="#">Capital and finance</a></li>
    <li><a href="#">About</a></li>
    <li><a href="#">Contact</a></li>
  </ul>
  <div class="bracket top"></div>
  <div class="bracket bottom"></div>
  <h1 class="hero-title">YOUR PROPERTY SOLUTION</h1>
  <a class="btn light" href="#" style="left:474px;top:414px;width:252px;height:50px">EXPLORE OUR PROJECTS
    <svg viewBox="0 0 18 14"><path d="M2 2l5 5-5 5M9 2l5 5-5 5" fill="none" stroke="currentColor" stroke-width="2"/></svg></a>
</header>

<section class="intro">
  <h2 class="intro-title">PELLIK – Family owned and operated,<br>community orientated</h2>
  <p class="intro-sub">Putting 45 years of local experience to work for the Inner West</p>

  <div class="photo" role="img" aria-label="Hands passing a small model house" style="left:80px;top:1028px;width:331px;height:206px;background:linear-gradient(135deg,#3a3e46,#c9c5c2 60%,#e9e2dc)"></div>
  <div class="photo" role="img" aria-label="Small tree growing on stacks of coins" style="left:435px;top:1028px;width:331px;height:206px;background:linear-gradient(180deg,#d9d4cc,#b3aea6 60%,#8d877d)"></div>
  <div class="photo" role="img" aria-label="Handshake over a signed contract with keys" style="left:789px;top:1028px;width:331px;height:206px;background:linear-gradient(135deg,#e9ecf1,#c6ccd6 60%,#2c2f36)"></div>

  <h3 class="card-title" style="left:80px">Leasing</h3>
  <h3 class="card-title" style="left:435px">Investment</h3>
  <h3 class="card-title" style="left:789px">Property Managment</h3>

  <p class="card-text" style="left:81px">Lorem Ipsum is simply dummy text of the printing and typesetting industry. Lorem Ipsum has been the industry's standard dummy text ever since the 1500s.</p>
  <p class="card-text" style="left:437px">Lorem Ipsum is simply dummy text of the printing and typesetting industry. Lorem Ipsum has been the industry's standard dummy text ever since the 1500s.</p>
  <p class="card-text" style="left:791px">Lorem Ipsum is simply dummy text of the printing and typesetting industry. Lorem Ipsum has been the industry's standard dummy text ever since the 1500s.</p>

  <a class="btn" href="#" style="left:81px;top:1432px;width:176px;height:45px">READ MORE <svg viewBox="0 0 18 14"><path d="M2 2l5 5-5 5M9 2l5 5-5 5" fill="none" stroke="currentColor" stroke-width="2"/></svg></a>
  <a class="btn" href="#" style="left:437px;top:1432px;width:176px;height:45px">READ MORE <svg viewBox="0 0 18 14"><path d="M2 2l5 5-5 5M9 2l5 5-5 5" fill="none" stroke="currentColor" stroke-width="2"/></svg></a>
  <a class="btn" href="#" style="left:791px;top:1432px;width:176px;height:45px">READ MORE <svg viewBox="0 0 18 14"><path d="M2 2l5 5-5 5M9 2l5 5-5 5" fill="none" stroke="currentColor" stroke-width="2"/></svg></a>
</section>

<section class="capital">
  <h2>Capital and finance</h2>
  <p>Lorem Ipsum is simply dummy text of the printing and typesetting industry. Lorem Ipsum has been the industry's standard dummy text ever since the 1500s, when an unknown printer took a galley of type and scrambled it to make a type specimen book. It has survived not only five centuries, but also the leap into electronic typesetting, remaining essentially unchanged.</p>
  <a class="btn light" href="#" style="left:81px;top:308px;width:176px;height:44px">READ MORE <svg viewBox="0 0 18 14"><path d="M2 2l5 5-5 5M9 2l5 5-5 5" fill="none" stroke="currentColor" stroke-width="2"/></svg></a>
</section>
<div class="photo" role="img" aria-label="Brick apartment building under a blue cloudy sky" style="left:607px;top:1557px;width:593px;height:397px;background:linear-gradient(180deg,#a9c3dc 0%,#d6e0e8 40%,#5f4b3e 65%,#7d7a74 100%)"></div>

<section class="projects">
  <h2 class="section-title" style="top:2022px">Recently Projects</h2>
  <div class="photo" role="img" aria-label="Two storey family house with green lawn" style="left:80px;top:2113px;width:335px;height:279px;background:linear-gradient(180deg,#2e64c4 0%,#bfb7a6 40%,#8e8a7c 75%,#4f8a2c 100%)"></div>
  <div class="photo" role="img" aria-label="Modern apartment tower with balconies" style="left:431px;top:2113px;width:337px;height:574px;background:linear-gradient(180deg,#1d6fd0 0%,#3d84d8 25%,#7f8790 55%,#4e5c50 100%)"></div>
  <div class="photo" role="img" aria-label="White apartment block with terraces" style="left:783px;top:2113px;width:337px;height:279px;background:linear-gradient(180deg,#2a7bd6 0%,#d9dee2 50%,#a8a59c 80%,#5d7a3a 100%)"></div>
  <div class="photo" role="img" aria-label="Industrial warehouse at sunset" style="left:80px;top:2410px;width:335px;height:277px;background:linear-gradient(180deg,#4d5f86 0%,#8893ab 45%,#6b6b70 75%,#56704a 100%)"></div>
  <div class="photo" role="img" aria-label="Modern red and white townhouses" style="left:783px;top:2410px;width:337px;height:277px;background:linear-gradient(180deg,#2f77d0 0%,#6fa3de 40%,#c9c4c2 65%,#b23b35 78%,#4d6a2e 100%)"></div>
  <a class="btn" href="#" style="left:477px;top:2744px;width:246px;height:44px">VIEW MORE PROJECTS <svg viewBox="0 0 18 14"><path d="M2 2l5 5-5 5M9 2l5 5-5 5" fill="none" stroke="currentColor" stroke-width="2"/></svg></a>
</section>

<section class="news" role="img" aria-label="Dimmed view of brick building with arched windows">
  <h2>Keep up to date</h2>
  <div class="field" style="top:163px;height:42px">Full Name</div>
  <div class="field" style="top:220px;height:42px">Phone#</div>
  <div class="field" style="top:277px;height:42px">Email Address</div>
  <div class="field msg" style="top:333px;height:132px">Message</div>
  <a class="btn light" href="#" style="left:508px;top:480px;width:186px;height:43px">SUBMIT NOW <svg viewBox="0 0 18 14"><path d="M2 2l5 5-5 5M9 2l5 5-5 5" fill="none" stroke="currentColor" stroke-width="2"/></svg></a>
</section>

<footer class="footer">
  <div class="logo">PELLIK</div>
  <a class="footer-links" href="#" style="left:415px;text-decoration:none">Terms of Use &amp; Privacy Policy</a>
  <span class="divider"></span>
  <a class="footer-links" href="#" style="left:680px;text-decoration:none">Customer Care</a>
  <span class="social" style="left:848px;background:var(--green)" role="img" aria-label="Social link"></span>
  <span class="social" style="left:890px" role="img" aria-label="Social link"></span>
  <span class="social" style="left:930px" role="img" aria-label="Social link"></span>
  <span class="social" style="left:969px" role="img" aria-label="Social link"></span>
  <span class="social" style="left:1013px" role="img" aria-label="Social link"></span>
  <span class="social" style="left:1052px" role="img" aria-label="Social link"></span>
  <p class="copyright">Copyright © 2019 Pellik.All Right Rresreved</p>
</footer>

</body>
</html>
```